Mailer Design - Packaging for Candy Company

I need packaging design for a mailer. This is for a candy company.

I've attached the box image and template, current size is 9x6x3. There may be a small change but at this point this is the correct size.

This should be a gift worthy package, fun, colorful, clean, professional, and will be photographed and used as a primary selling point.

Industry/Entity Type

It Company

Colors
00a990
a9d046
fbed22
f78f20
f37122
ec1f27
e34197
0455a3
6b449b

Requirements
Must have
• Packaging should incorporate:
• Mira Bee's Candy
• Sugarhaven, WA
• www.MiraBeesCandy.example
Nice to have
• I've attached three files with aspects that I like.
• Image 1- I like the different styles on the sides and top of the box. I like the multi-width stripes
• Image 2- I like the stripes
• Image 3- I like the badge style
• While these are aspects I like I am willing to take suggestions. I want to portray a bright, fun, candy company with a gift quality box.

```html
<!DOCTYPE html>
<html lang="en">
<head>
<meta charset="utf-8">
<title>Mira Bee's Candy – Mailer Box Dieline</title>
<link rel="stylesheet" href="https://fonts.googleapis.com/css2?family=Oswald:wght@400&family=Open+Sans:wght@700&family=Crimson+Text:wght@400&display=swap">
<style>
  :root {
    --magenta: #ec008c;
    --purple: #7b3f98;
    --deep-purple: #a3238e;
    --green: #22b05f;
    --lime: #a9d046;
    --yellow: #ffde00;
    --amber: #fbb61a;
    --orange: #f26522;
    --sky: #8cd7f7;
    --white: #ffffff;
    --paper: #ffffff;
  }
  html, body {
    margin: 0;
    padding: 0;
    width: 1200px;
    height: 602px;
    overflow: hidden;
    background: var(--paper);
  }
  .dieline {
    position: relative;
    width: 1200px;
    height: 602px;
  }
  .panel {
    position: absolute;
    box-sizing: border-box;
  }
  .panel--top {
    left: 420px; top: 68px; width: 362px; height: 116px;
    background: linear-gradient(to right,
      var(--green) 0 10%, var(--magenta) 10% 22%, var(--yellow) 22% 30%,
      var(--orange) 30% 44%, var(--sky) 44% 52%, var(--lime) 52% 62%,
      var(--deep-purple) 62% 70%, var(--amber) 70% 84%,
      var(--magenta) 84% 92%, var(--yellow) 92% 100%);
  }
  .panel--left {
    left: 298px; top: 190px; width: 116px; height: 234px;
    background: linear-gradient(to bottom,
      var(--orange) 0 12%, var(--sky) 12% 20%, var(--lime) 20% 34%,
      var(--deep-purple) 34% 42%, var(--yellow) 42% 56%,
      var(--magenta) 56% 66%, var(--green) 66% 84%, var(--amber) 84% 100%);
  }
  .panel--right {
    left: 788px; top: 190px; width: 116px; height: 234px;
    background: linear-gradient(to bottom,
      var(--yellow) 0 14%, var(--green) 14% 24%, var(--magenta) 24% 38%,
      var(--sky) 38% 50%, var(--amber) 50% 58%, var(--deep-purple) 58% 72%,
      var(--orange) 72% 86%, var(--lime) 86% 100%);
  }
  .panel--bottom {
    left: 420px; top: 430px; width: 362px; height: 110px;
    background: linear-gradient(to right,
      var(--deep-purple) 0 8%, var(--yellow) 8% 20%, var(--sky) 20% 34%,
      var(--magenta) 34% 42%, var(--green) 42% 56%, var(--orange) 56% 64%,
      var(--lime) 64% 78%, var(--amber) 78% 88%, var(--magenta) 88% 100%);
  }
  .panel--lid {
    left: 420px; top: 190px; width: 362px; height: 234px;
    background: var(--magenta);
    display: flex;
    align-items: center;
    justify-content: center;
  }
  .badge {
    width: 226px;
    height: 170px;
    box-sizing: border-box;
    background: var(--purple);
    border: 3px solid var(--white);
    border-radius: 22px;
    display: flex;
    flex-direction: column;
    align-items: center;
    justify-content: center;
    color: var(--white);
    text-align: center;
  }
  .badge__name {
    margin: 0;
    font-family: 'Oswald', sans-serif;
    font-weight: 400;
    font-size: 34px;
    line-height: 1.1;
    color: var(--white);
  }
  .badge__location {
    margin: 8px 0 0;
    font-family: 'Crimson Text', serif;
    font-size: 10px;
    letter-spacing: 0.5px;
    color: var(--white);
  }
  .website {
    position: absolute;
    left: 0; right: 0; bottom: 16px;
    margin: 0;
    text-align: center;
    font-family: 'Open Sans', sans-serif;
    font-weight: 700;
    font-size: 12px;
    color: var(--white);
  }
</style>
</head>
<body>
  <main class="dieline">
    <section class="panel panel--top" aria-label="Top flap stripes"></section>
    <section class="panel panel--left" aria-label="Left side stripes"></section>
    <section class="panel panel--lid">
      <div class="badge">
        <h1 class="badge__name">Mira Bee's<br>Candy</h1>
        <p class="badge__location">SUGARHAVEN, WA</p>
      </div>
    </section>
    <section class="panel panel--right" aria-label="Right side stripes"></section>
    <section class="panel panel--bottom">
      <p class="website">www.MiraBeesCandy.example</p>
    </section>
  </main>
</body>
</html>
```